Meridale Legal Letterhead for Law firm must be modern and use the logo I uploaded.

Hello I want a clean modern professional letterhead for my law firm Meridale Legal. A logo has already been created and all files have been uploaded. The information for the firm can be given through message. Please use the logo that has already been created. Please also use the color scheme of that logo. (blue and white).

Target Market(s)

General Public

Industry/Entity Type

Law Firm

Colors

Designer to choose colors to be used in the design.

Requirements
Must have
• This must be a modern professional letterhead
Nice to have
• My logo that is included in file form
Should not have
• Should not have logo that is not the one I uploaded.

```html
<!DOCTYPE html>
<html lang="en">
<head>
<meta charset="utf-8">
<title>Meridale Legal Letterhead</title>
<link href="https://fonts.googleapis.com/css2?family=Lato:wght@400;700&family=Montserrat:wght@400;700&family=Open+Sans:wght@600&family=Questrial&display=swap" rel="stylesheet">
<style>
  :root {
    --navy: #2c3361;
    --grey-line: #a7a9ac;
    --grey-text: #9a9a9c;
    --body-text: #8e8f92;
    --contact-text: #555558;
    --paper: #ffffff;
    --backdrop: #242424;
  }
  * { margin: 0; padding: 0; box-sizing: border-box; }
  html, body { width: 1051px; height: 1200px; overflow: hidden; background: var(--backdrop); }
  .letterhead {
    position: absolute; left: 98px; top: 0;
    width: 855px; height: 1200px;
    background: var(--paper);
    overflow: hidden;
  }
  .brand-mark {
    position: absolute; left: 101px; top: 32px;
    width: 40px; height: 40px; background: var(--navy);
  }
  .brand-name {
    position: absolute; left: 36px; top: 105px;
    font-family: "Montserrat", sans-serif; font-weight: 700;
    font-size: 13px; line-height: 16px; letter-spacing: 5px; color: var(--navy);
    white-space: nowrap;
  }
  .firm-contact {
    position: absolute; right: 28px; top: 38px;
    list-style: none;
    font-family: "Lato", sans-serif; font-size: 13px; color: var(--contact-text);
  }
  .firm-contact li {
    display: flex; align-items: center; justify-content: flex-end; gap: 5px;
    height: 17px; margin-bottom: 10px;
  }
  .icon { width: 17px; height: 17px; display: block; flex: none; }
  .header-rule, .footer-band { position: absolute; left: 0; }
  .header-rule { top: 126px; }
  .footer-band { top: 1131px; }
  .footer-address {
    position: absolute; left: 36px; top: 1140px;
    display: flex; align-items: center; gap: 6px;
    font-family: "Lato", sans-serif; font-size: 13.5px; color: #fff;
  }
  .recipient { position: absolute; left: 41px; top: 248px; font-family: "Montserrat", sans-serif; color: var(--grey-text); }
  .recipient-name { font-weight: 700; font-size: 26px; line-height: 1; margin-bottom: 13px; letter-spacing: 0.3px; }
  .recipient-line { font-weight: 400; font-size: 15px; line-height: 20px; margin-bottom: 8px; }
  .recipient-line.address { margin-bottom: 0; }
  .letter-date {
    position: absolute; right: 38px; top: 358px;
    font-family: "Open Sans", sans-serif; font-weight: 600; font-size: 17px; line-height: 22px; color: var(--grey-text);
  }
  .body-paragraph {
    position: absolute; left: 37px; width: 781px;
    font-family: "Questrial", sans-serif; font-size: 16.4px; line-height: 19.7px;
    color: var(--body-text); text-align: justify; text-align-last: left;
    hyphens: auto; -webkit-hyphens: auto;
  }
  .body-paragraph.first { top: 418px; }
  .body-paragraph.second { top: 556px; }
  .body-paragraph.third { top: 694px; }
  .signoff {
    position: absolute; left: 65px; top: 817px;
    font-family: "Questrial", sans-serif; font-size: 22px; line-height: 28px; color: var(--grey-text);
  }
  .signature {
    position: absolute; left: 84px; top: 866px; width: 158px; height: 97px;
    background: linear-gradient(135deg, #f1f1f2, #e6e6e8);
  }
</style>
</head>
<body>
<div class="letterhead">
  <span class="brand-mark"></span>
  <span class="brand-name">MERIDALE LEGAL</span>

  <ul class="firm-contact">
    <li>+00 214 555 37
      <svg class="icon" viewBox="0 0 17 17"><rect width="17" height="17" rx="2" fill="var(--navy)"/><path d="M5 3.5l2 2.3-1.1 1.4c.7 1.5 1.8 2.6 3.3 3.3l1.4-1.1 2.3 2-1.2 2c-4.3-.3-7.6-3.6-7.9-7.9z" fill="#fff"/></svg>
    </li>
    <li>office@meridalelegal.com
      <svg class="icon" viewBox="0 0 17 17"><rect width="17" height="17" rx="2" fill="var(--navy)"/><rect x="3" y="4.5" width="11" height="8" fill="none" stroke="#fff" stroke-width="1.2"/><path d="M3 4.5l5.5 4.5 5.5-4.5M3 12.5l4-3.5M14 12.5l-4-3.5" fill="none" stroke="#fff" stroke-width="1.1"/></svg>
    </li>
    <li>www.meridalelegal.com
      <svg class="icon" viewBox="0 0 17 17"><rect width="17" height="17" rx="2" fill="var(--navy)"/><path d="M6 3.5v9.5l2.2-2.2 1.6 3.4 1.4-.7-1.6-3.3h3.1z" fill="#fff"/></svg>
    </li>
  </ul>

  <svg class="header-rule" width="855" height="20" viewBox="0 0 855 20">
    <rect x="0" y="16" width="482" height="2" fill="var(--grey-line)"/>
    <polygon points="500,0 514,0 501,18 486,18" fill="var(--grey-line)"/>
    <polygon points="518,0 531,0 517,18 505,18" fill="var(--grey-line)"/>
    <polygon points="534,0 855,0 855,18 523,18" fill="var(--navy)"/>
  </svg>

  <div class="recipient">
    <p class="recipient-name">ELENA WARD</p>
    <p class="recipient-line">0142-555-318</p>
    <p class="recipient-line">hello@elenaward.com</p>
    <p class="recipient-line address">5820 Harbor View Ln. Suite<br>210 Dallas, TX 75201</p>
  </div>
  <p class="letter-date">12 December, 2023</p>

  <p class="body-paragraph first">Lorem ipsum dolor sit amet, consectetuer adipiscing elit, sed diam nonummy nibh euismod tincidunt ut laoreet dolore magna aliquam erat volutpat. Ut wisi enim ad minim veniam, quis nostrud exerci tation ullamcorper suscipit lobortis nisl ut aliquip ex ea commodo consequat. Duis autem vel eum iriure dolor in hendrerit in vulputate velit esse molestie consequat, vel illum dolore eu feugiat nulla facilisis at vero eros et accumsan et iusto odio dignissim qui blandit praesent luptatum zzril delenit augue duis dolore te feugait nulla facilisi.</p>
  <p class="body-paragraph second">Lorem ipsum dolor sit amet, cons ectetuer adipiscing elit, sed diam nonummy nibh euismod tincidunt ut laoreet dolore magna aliquam erat volutpat. Ut wisi enim ad minim veniam, quis nostrud exerci tation ullamcorper suscipit lobortis nisl ut aliquip ex ea commodo consequat.<br>Lorem ipsum dolor sit amet, consectetuer adipiscing elit, sed diam nonummy nibh euismod tincidunt ut laoreet dolore magna aliquam erat</p>
  <p class="body-paragraph third">Lorem ipsum dolor sit amet, cons ectetuer adipiscing elit, sed diam nonummy nibh euismod tincidunt ut laoreet dolore magna aliquam erat volutpat. Ut wisi enim ad minim veniam, quis nostrud exerci tation ullamcorper suscipit lobortis nisl ut aliquip ex ea commodo consequat. Lorem ipsum dolor sit zamet, consectetuer adipiscing elit, sed diam nonummy nibh euismod tincidunt.</p>

  <p class="signoff">Managing Director</p>
  <div class="signature" role="img" aria-label="Handwritten signature of the managing director"></div>

  <svg class="footer-band" width="855" height="35" viewBox="0 0 855 35">
    <polygon points="0,0 540,0 555,35 0,35" fill="var(--navy)"/>
    <polygon points="560,0 575,0 592,35 577,35" fill="var(--navy)"/>
    <polygon points="597,0 612,0 629,35 614,35" fill="var(--navy)"/>
    <polygon points="633,0 648,0 665,35 650,35" fill="var(--navy)"/>
  </svg>
  <div class="footer-address">
    <svg class="icon" viewBox="0 0 17 17"><rect width="17" height="17" rx="2" fill="#fff"/><path d="M8.5 2.5a4 4 0 0 0-4 4c0 3 4 8 4 8s4-5 4-8a4 4 0 0 0-4-4z" fill="var(--navy)"/><circle cx="8.5" cy="6.5" r="1.5" fill="#fff"/></svg>
    <span>2170 Linden Park Avenue Washington, DC 20019</span>
  </div>
</div>
</body>
</html>
```